Kerno Solutions: searching for a flyer to trow in letterboxes for properties we are interested in

Hello ,

Introduction:
We are a company based in Luxembourg called "Kerno Solutions". We are specialized in buying properties on which we develop and build constructions before selling them.

Informations for the flyer:
We need a flyer to trow into the letter boxes of property owners letting them know that we are interested in buying their property, if they are interested they can give us a call.

The text for the flyer/letter is in the attachment called >>2020-03-11_KS_Text for flyer,letter there might be slight changes<<.

We need to look competent, professional and financially stable.

The flyer needs to be short and not over welling with information otherwise it will land in the trash.

We have decided that we don't want real pictures on the flyer, but shapes of any kind, blue prints, drawings are fine.

Format should be in DIN A4. We plan to print the flyer on both sides in two different languages, in other words the design will be the same on both sides only the text will be in a different language.

I also added our current logo and here is the design of the website that is under construction at the moment http://www.kernosolutions-example.lu/. The logo's color can be changed into a different blue or uni color (all white or all black).
Updates

Hi, First time user the howl thing started faster as expected. Furthermore, I need to catch my boss to discust the project with him and he is on a lot of meetings. Please give us a little bit more time. Thanks

Target Market(s)

Property owners

Requirements
Must have
• email, phone number, tax number (RCS), Tax number , matriculation and address.
see word file in attachment for information
Nice to have
• Our company logo, in one form or an other, you can be creative, the logo is in the attachment.
Should not have
• Real pictures

```html
<!DOCTYPE html>
<html lang="en">
<head>
<meta charset="utf-8">
<title>Kerno Solutions – Property Flyer</title>
<link href="https://fonts.googleapis.com/css2?family=Oswald:wght@500;700&family=Source+Sans+3:wght@400;600&display=swap" rel="stylesheet">
<style>
  :root{
    --stage:#c4c5c7;
    --paper:#ffffff;
    --paper-shade:#eceef0;
    --brand-blue:#22568a;
    --band-blue:#1f5282;
    --ink:#111111;
    --on-band:#ffffff;
    --on-band-soft:rgba(255,255,255,.78);
    --photo-light:#b9bbbd;
    --photo-dark:#4a4c4f;
  }
  *{box-sizing:border-box;margin:0;padding:0}
  html,body{width:1200px;height:675px;overflow:hidden;background:var(--stage)}
  .flyer{
    position:absolute;left:150px;top:19px;width:900px;height:636px;
    background:linear-gradient(180deg,var(--paper-shade) 0%,var(--paper) 40%);
    overflow:hidden;box-shadow:0 6px 18px rgba(0,0,0,.18);
  }
  .brand{
    position:absolute;left:60px;top:48px;display:flex;align-items:center;gap:16px;
  }
  .brand-square{width:38px;height:38px;background:var(--brand-blue)}
  .brand-name{
    font-family:"Oswald",sans-serif;font-weight:700;font-size:40px;
    letter-spacing:.5px;color:var(--brand-blue);text-transform:uppercase;line-height:1;
  }
  .headline{
    position:absolute;left:60px;top:140px;width:430px;
    font-family:"Oswald",sans-serif;font-weight:700;font-size:52px;line-height:1.1;
    text-transform:uppercase;color:var(--ink);white-space:nowrap;
  }
  .headline .accent{color:var(--brand-blue)}
  .headline .cta{margin-top:14px;display:block}
  .visual{
    position:absolute;left:520px;top:110px;right:0;bottom:200px;
    background:radial-gradient(ellipse at 45% 65%,var(--photo-light) 0%,#8e9093 45%,var(--photo-dark) 100%);
  }
  .contact-band{
    position:absolute;left:0;right:0;bottom:0;height:200px;background:var(--band-blue);
    color:var(--on-band);padding:36px 60px 22px;
    display:flex;flex-direction:column;justify-content:space-between;
  }
  .contact-row{display:flex;align-items:flex-start;justify-content:space-between}
  .contact-group{display:flex;flex-direction:column;gap:12px}
  .contact-line{display:flex;align-items:center;gap:10px}
  .contact-big{
    font-family:"Oswald",sans-serif;font-weight:500;font-size:32px;line-height:1;letter-spacing:.5px;white-space:nowrap;
  }
  .contact-small{
    font-family:"Source Sans 3",sans-serif;font-weight:400;font-size:20px;line-height:1;white-space:nowrap;
  }
  .social{display:flex;align-items:center;gap:10px;align-self:flex-end}
  .social-dot{width:20px;height:20px;border-radius:50%;background:var(--on-band)}
  .icon{width:28px;height:28px;flex:none}
  .legal{
    font-family:"Source Sans 3",sans-serif;font-weight:400;font-size:13px;line-height:1.3;
    color:var(--on-band-soft);white-space:nowrap;border-top:1px solid rgba(255,255,255,.3);padding-top:10px;
  }
</style>
</head>
<body>
  <main class="flyer">
    <header class="brand">
      <span class="brand-square"></span>
      <span class="brand-name">Kerno Solutions</span>
    </header>

    <h1 class="headline">
      Need to sell<br>
      <span class="accent">your property?</span>
      <span class="cta">Call us today!</span>
    </h1>

    <div class="visual" role="img" aria-label="Photo of a small model house with a set of house keys on a wooden table, in greyscale with blue walls"></div>

    <footer class="contact-band">
      <div class="contact-row">
        <div class="contact-group">
          <div class="contact-line">
            <svg class="icon" viewBox="0 0 28 28" aria-hidden="true">
              <rect x="1" y="1" width="26" height="26" rx="5" fill="#fff"/>
              <path d="M9 6c1 0 2 3 2 4s-1.5 1.5-1 3 2.5 4 4 4.5 2-1 3-1 4 1 4 2-1.5 3-3 3C11 21.5 6.5 15 6.5 9 6.5 7.5 8 6 9 6z" fill="#1f5282"/>
            </svg>
            <span class="contact-big">1.800.555.0142</span>
          </div>
          <div class="contact-line">
            <svg class="icon" viewBox="0 0 28 28" aria-hidden="true">
              <rect x="2" y="6" width="24" height="16" fill="none" stroke="#fff" stroke-width="1.6"/>
              <path d="M2 6l12 9 12-9M2 22l9-8M26 22l-9-8" fill="none" stroke="#fff" stroke-width="1.6"/>
            </svg>
            <span class="contact-small">info@kernosolutions-example.lu</span>
          </div>
        </div>

        <div class="contact-group">
          <span class="contact-big">FAX: 187.654.0199</span>
          <span class="contact-small">www.kernosolutions-example.lu</span>
        </div>

        <div class="social">
          <span class="social-dot"></span>
          <span class="contact-small">kernosolutions</span>
        </div>
      </div>

      <p class="legal">12 Rue de l’Exemple, L-1234 Luxembourg · RCS B000000 · TVA LU00000000 · Matricule 2020 0000 000</p>
    </footer>
  </main>
</body>
</html>
```